Improve Design and Readability of Existing Web Page

Corvantia.org is a free educational radiology resource with one of the web's largest collections of radiology cases and reference articles. This job involves improving the design of the article pages to make the text more readable.
We want a new design for the body of the article page that has considered at least: the typeface, vertical rhythm, line length, line height and styling of the text, headings and other standard HTML elements. IMPORTANT: You would only be designing the content area of the page, inside the existing layout, as indicated here: http://q.zx/i/Tk4W
If you are the successful applicant you'll have your work featured across the 6000+ article pages on the site.
The HTML elements that you will need to consider in your design are:
* Headings (three levels)
* Paragraphs
* Superscript and Subscript text
* Ordered and unordered lists, potentially nested multiple levels deep
* Links to other corvantia content (blue links)
* Links to other corvantia content that does not yet exist (grey links)
The articles are accessible at: http://corvantia.org/encyclopaedia/all/all
Sample articles that can be used for reference and as a base for the redesign:
* http://corvantia.org/articles/neurosarcoidosis
* http://corvantia.org/articles/golden_s_sign
* http://corvantia.org/articles/fetal-heart-rate
* http://corvantia.org/articles/meningioma

```html
<!DOCTYPE html>
<html lang="en">
<head>
<meta charset="utf-8">
<title>Corvantia.org – Article Typography Styles</title>
<link href="https://fonts.googleapis.com/css2?family=Arimo:ital,wght@0,400;0,700;1,400;1,700&display=swap" rel="stylesheet">
<style>
  :root {
    --text: #222222;
    --heading: #2b2b2b;
    --link: #3e6795;
    --panel-blue: #3f6593;
    --panel-purple: #452c63;
    --outline-text: #3d2466;
    --outline-rule: #a79fb8;
    --white: #ffffff;
    --page: #ffffff;
  }
  * { box-sizing: border-box; margin: 0; padding: 0; }
  html, body {
    width: 1200px; height: 2523px; overflow: hidden;
    background: var(--page);
    font-family: "Arimo", Arial, sans-serif;
    color: var(--text);
  }
  .sheet { position: relative; width: 1200px; height: 2523px; }
  .block { position: absolute; left: 251px; width: 667px; }

  .heading { font-family: "Arimo", Helvetica, sans-serif; font-weight: 700; color: var(--heading); position: absolute; left: 251px; line-height: 1; white-space: nowrap; }
  .h1 { font-size: 28px; top: 97px; }
  .h2 { font-size: 25px; top: 163px; }
  .h3 { font-size: 22px; top: 225px; }
  .h4 { font-size: 20px; top: 282px; }
  .h5 { font-size: 17px; top: 342px; }

  .spec-label { font-weight: 700; font-size: 14px; line-height: 22px; }
  .paragraph { font-size: 14px; line-height: 22.5px; width: 660px; }
  .paragraph + .paragraph { margin-top: 22px; }

  .list-block { left: 276px; width: 640px; }
  .list-block .spec-label { line-height: 30px; margin-bottom: 0; }
  .list { list-style: none; font-size: 14px; line-height: 30.5px; }
  .list li::before { content: "•"; margin-right: 5px; }
  .list .nested { list-style: none; padding-left: 10px; }
  .numbered { list-style: none; font-size: 14px; line-height: 30.5px; counter-reset: item; }
  .numbered li { counter-increment: item; }
  .numbered li::before { content: counter(item) " "; }

  .link-sample { font-size: 13px; line-height: 23px; font-weight: 700; color: var(--text); text-decoration: underline; display: block; }
  .link-hover { text-decoration: underline; }
  .emphasis { font-size: 13px; font-weight: 700; font-style: italic; line-height: 22px; }

  .accordion-outline .row {
    height: 62px; border-bottom: 2px solid var(--outline-rule);
    display: flex; align-items: center; justify-content: space-between;
    padding: 10px 8px 0 12px; color: var(--outline-text); font-weight: 700; font-size: 13px;
  }
  .accordion-solid .row {
    height: 46px; display: flex; align-items: center; justify-content: space-between;
    padding: 0 8px 0 12px; color: var(--white); font-weight: 700; font-size: 13px;
    background: var(--panel-blue);
  }
  .accordion-solid .row + .row { border-top: 2px solid var(--white); }
  .accordion-solid .row.open { background: var(--panel-purple); }
  .accordion-body { font-size: 14px; line-height: 22.5px; padding: 32px 12px 26px 14px; }
  .icon { width: 18px; height: 18px; }
</style>
</head>
<body>
<main class="sheet">
  <h1 class="heading h1">H1&nbsp; - Helvetica, 26px, bold</h1>
  <h2 class="heading h2">H2&nbsp; - Helvetica, 23px, bold</h2>
  <h3 class="heading h3">H3&nbsp; - Helvetica, 21px, bold</h3>
  <h4 class="heading h4">H4&nbsp; - Helvetica, 19px, bold</h4>
  <h5 class="heading h5">H5&nbsp; - Helvetica, 17px, bold</h5>

  <section class="block" style="top:427px">
    <p class="spec-label">Paragraph - Arial 13px, line height, 21px</p>
    <p class="paragraph">Lorem Ipsum is simply dummy text of the printing and typesetting industry. Lorem ipsum has been the industry's standard dummy text ever since the 1500s, when an unknown printer took a galley of type and scrambled it to make a type specimen book.</p>
    <p class="paragraph">It has survived not only five centuries, but also the leap into electronic typesetting, remaining essentially unchanged. It was popularised in the 1960s with the release of Varnetex sheets containing.</p>
  </section>

  <section class="block list-block" style="top:702px">
    <p class="spec-label">Bulleted List - Arial, 13px, line height 24px</p>
    <ul class="list">
      <li>Nunc varius sapien non ullamcorper gravida.</li>
      <li>Integer pulvinar justo vitae dui imperdiet, aliquet pulvinar risus volutpat.</li>
      <li>Nam et nisl et nisl elementum iaculis ut sed ipsum.</li>
      <li>Phasellus lacinia massa lacinia, rutrum mi ac, accumsan metus.</li>
    </ul>
  </section>

  <section class="block list-block" style="top:906px">
    <p class="spec-label">Bulleted List second level - Arial, 13px, line height 24px</p>
    <ul class="list">
      <li>Nunc varius sapien non ullamcorper gravida.
        <ul class="nested">
          <li>Integer pulvinar justo vitae dui imperdiet, aliquet pulvinar risus volutpat.</li>
          <li>Nam et nisl et nisl elementum iaculis ut sed ipsum.</li>
          <li>Phasellus lacinia massa lacinia, rutrum mi ac, accumsan metus.</li>
        </ul>
      </li>
      <li>Integer pulvinar justo vitae dui imperdiet, aliquet pulvinar risus volutpat.</li>
      <li>Nam et nisl et nisl elementum iaculis ut sed ipsum.</li>
      <li>Vestibulum facilisis est commodo, posuere massa ut, elementum velit.</li>
    </ul>
  </section>

  <section class="block list-block" style="top:1204px">
    <p class="spec-label">Numbered List - Arial, 13px, line height 24px</p>
    <ol class="numbered">
      <li>Nunc varius sapien non ullamcorper gravida.</li>
      <li>Integer pulvinar justo vitae dui imperdiet, aliquet pulvinar risus volutpat.</li>
      <li>Nam et nisl et nisl elementum iaculis ut sed ipsum.</li>
      <li>Phasellus lacinia massa lacinia, rutrum mi ac, accumsan metus.</li>
    </ol>
  </section>

  <section class="block" style="top:1419px">
    <a class="link-sample" href="#">TEXT LINK NORMAL - Lorem ipsum dolor sit amet, consectetur adipiscing elit. - #3e6795</a>
    <a class="link-sample link-hover" href="#">TEXT LINK HOVER - Lorem ipsum dolor sit amet, consectetur adipiscing elit. - #3e6795</a>
  </section>

  <section class="block" style="top:1495px">
    <a class="link-sample" href="#">Lorem Ipsum is simply dummy text of the printing and typesetting</a>
    <a class="link-sample" href="#">Lorem Ipsum is simply dummy text of the printing and typesetting</a>
  </section>

  <p class="block emphasis" style="top:1574px">Lorem Ipsum is simply dummy text of the printing and typesetting</p>

  <section class="block accordion-outline" style="top:1660px">
    <div class="row"><span>References</span><svg class="icon" viewBox="0 0 18 18"><path d="M9 2v14M2 9h14" stroke="currentColor" stroke-width="1.6"/></svg></div>
    <div class="row"><span>References</span><svg class="icon" viewBox="0 0 18 18"><path d="M9 2v14M2 9h14" stroke="currentColor" stroke-width="1.6"/></svg></div>
    <div class="row"><span>References</span><svg class="icon" viewBox="0 0 18 18"><path d="M9 2v14M2 9h14" stroke="currentColor" stroke-width="1.6"/></svg></div>
  </section>

  <section class="block accordion-solid" style="top:1903px">
    <div class="row"><span>References</span><svg class="icon" viewBox="0 0 18 18"><path d="M9 2v14M2 9h14" stroke="currentColor" stroke-width="2"/></svg></div>
    <div class="row"><span>References</span><svg class="icon" viewBox="0 0 18 18"><path d="M9 2v14M2 9h14" stroke="currentColor" stroke-width="2"/></svg></div>
    <div class="row"><span>References</span><svg class="icon" viewBox="0 0 18 18"><path d="M9 2v14M2 9h14" stroke="currentColor" stroke-width="2"/></svg></div>
  </section>

  <section class="block accordion-solid" style="top:2115px">
    <div class="row"><span>References</span><svg class="icon" viewBox="0 0 18 18"><path d="M9 2v14M2 9h14" stroke="currentColor" stroke-width="2"/></svg></div>
    <div class="row open"><span>References</span><svg class="icon" viewBox="0 0 18 18"><path d="M2 9h14" stroke="currentColor" stroke-width="2"/></svg></div>
    <div class="accordion-body">Lorem Ipsum is simply dummy text of the printing and typesetting industry. Lorem ipsum has been the industry's standard dummy text ever since the 1500s, when an unknown printer took a galley of type and scrambled it to make a type specimen book.</div>
    <div class="row"><span>References</span><svg class="icon" viewBox="0 0 18 18"><path d="M9 2v14M2 9h14" stroke="currentColor" stroke-width="2"/></svg></div>
  </section>
</main>
</body>
</html>
```